Create a book cover for zorvex QPL

We are looking for a designer to design a cover for a log book in two versions. The two versions only have a slight difference in page count and text, other than that, it is one design.

The main color is blue. No black, no white except book title and other text. The cover must closely relate to the interior pages provided in the attachment. The style should be simple and modern, no old school graphics and fonts. Apply color psychology in the design. Please be creative and you are allowed to use download templates and graphic elements, but you must provide commercial licenses.

Here are the basic information of the book:
1. Book title: GARAGE SEASONS NOTE JOURNAL
2. Book size: 6x9 inches
3. Page count: 61 (version 1) and 73 (version 2)
4. Platform: zorvex qpl

Requirement for version 1:
1. Front cover: book title
2. Spine: no book title and author name
3. Back cover: text on the top and pen name logo on the bottom middle
4. Back cover text:
• Your essential tool for tracking vehicle health and maintenance
• Dedicated sections for maintenance schedules and repair history
• Track up to 30 maintenance schedules and repair history
• Easy-to-use tables and clear layouts
• Perfect for all car owners, from enthusiasts to everyday drivers

We hope it helps you keep your vehicle in excellent condition. Please take a moment to leave a positive review on Zorvex and share your experience if you find it helpful. Thank you!

Requirement for version 2:
1. Front cover: book title ,text "COLOR PAGES"
4. Back cover text:
• Track up to 36 maintenance schedules and repair history

Export:
1. Cover design in PDF and editable file format.
2. Sources/Commercial licenses for everything you did not create by yourself including fonts.

```html
<!DOCTYPE html>
<html lang="en">
<head>
<meta charset="utf-8">
<title>Garage Seasons Note Journal – Cover</title>
<link rel="stylesheet" href="https://fonts.googleapis.com/css2?family=Antonio:wght@700&family=Montserrat:wght@500;600&display=swap">
<style>
  :root {
    --cover-blue: #00309a;
    --title-yellow: #fff10a;
    --text-white: #ffffff;
    --badge-dark: #1d283b;
    --badge-ring: #9aa1ab;
  }
  * { margin: 0; padding: 0; box-sizing: border-box; }
  html, body { width: 1200px; height: 896px; overflow: hidden; background: var(--cover-blue); }
  .cover {
    position: relative;
    width: 1200px;
    height: 896px;
    background: var(--cover-blue);
    font-family: "Montserrat", sans-serif;
    color: var(--text-white);
  }
  .cover-art { position: absolute; inset: 0; }
  .title-type { font-family: "Antonio", sans-serif; font-weight: 700; }
  .title-yellow { fill: var(--title-yellow); }
  .title-blue { fill: var(--cover-blue); }
  .title-band { fill: var(--text-white); }
  .photo-ring { fill: none; stroke: var(--title-yellow); stroke-width: 6; }
  .badge-disc { fill: var(--badge-dark); stroke: var(--badge-ring); stroke-width: 4; }
  .badge-name { font-family: "Montserrat", sans-serif; font-weight: 600; fill: var(--text-white); }

  .back-features {
    position: absolute;
    left: 30px;
    top: 318px;
    list-style: none;
    font-size: 15.2px;
    font-weight: 500;
    letter-spacing: 0.3px;
  }
  .back-features li { height: 34px; line-height: 22px; }
  .back-features li::before { content: "•"; margin-right: 6px; }
  .back-message {
    position: absolute;
    left: 30px;
    top: 506px;
    width: 560px;
    font-size: 15.2px;
    font-weight: 500;
    line-height: 20px;
    letter-spacing: 0.3px;
  }
</style>
</head>
<body>
<main class="cover">
  <svg class="cover-art" width="1200" height="896" viewBox="0 0 1200 896" xmlns="http://www.w3.org/2000/svg">
    <defs>
      <radialGradient id="photo-oil" cx="50%" cy="50%" r="60%">
        <stop offset="0" stop-color="#a88a4a"/><stop offset="1" stop-color="#3c4048"/>
      </radialGradient>
      <linearGradient id="photo-showroom" x1="0" y1="0" x2="0" y2="1">
        <stop offset="0" stop-color="#e6e8ea"/><stop offset="1" stop-color="#b9c4cc"/>
      </linearGradient>
      <radialGradient id="photo-inspection" cx="50%" cy="50%" r="60%">
        <stop offset="0" stop-color="#9ea3aa"/><stop offset="1" stop-color="#3e434c"/>
      </radialGradient>
      <clipPath id="clip-a"><circle cx="716" cy="738" r="81"/></clipPath>
    </defs>

    <!-- Back cover title -->
    <g class="back-title title-type">
      <text class="title-yellow" x="194" y="128" font-size="104" textLength="198" lengthAdjust="spacingAndGlyphs">GARAGE</text>
      <rect class="title-band" x="202" y="144" width="190" height="55"/>
      <text class="title-blue" x="214" y="194" font-size="54" textLength="159" lengthAdjust="spacingAndGlyphs">SEASONS</text>
      <text class="title-yellow" x="194" y="304" font-size="104" textLength="199" lengthAdjust="spacingAndGlyphs">NOTE JOURNAL</text>
    </g>

    <!-- Pen name badge -->
    <g class="pen-name-badge">
      <circle class="badge-disc" cx="302" cy="722" r="69"/>
      <text class="badge-name" x="302" y="729" font-size="19" text-anchor="middle">TOBIN VALE</text>
    </g>

    <!-- Front cover title -->
    <g class="front-title title-type">
      <text class="title-yellow" x="700" y="251" font-size="210" textLength="400" lengthAdjust="spacingAndGlyphs">GARAGE</text>
      <rect class="title-band" x="716" y="286" width="385" height="110"/>
      <text class="title-blue" x="741" y="388" font-size="112" textLength="322" lengthAdjust="spacingAndGlyphs">SEASONS</text>
      <text class="title-yellow" x="700" y="609" font-size="210" textLength="405" lengthAdjust="spacingAndGlyphs">NOTE JOURNAL</text>
    </g>

    <!-- Front cover photo circles -->
    <g class="front-photos">
      <circle cx="716" cy="738" r="81" fill="url(#photo-oil)" role="img" aria-label="Photo: fresh oil being poured into a car engine"/>
      <circle class="photo-ring" cx="716" cy="738" r="81"/>
      <circle cx="896" cy="738" r="81" fill="url(#photo-showroom)" role="img" aria-label="Photo: dealer and customer shaking hands in a car showroom"/>
      <circle class="photo-ring" cx="896" cy="738" r="81"/>
      <circle cx="1077" cy="738" r="81" fill="url(#photo-inspection)" role="img" aria-label="Photo: mechanic writing on a clipboard over an engine bay"/>
      <circle class="photo-ring" cx="1077" cy="738" r="81"/>
    </g>
  </svg>

  <ul class="back-features">
    <li>Your essential tool for tracking vehicle health and maintenance</li>
    <li>Dedicated sections for maintenance schedules and repair history</li>
    <li>Track up to 30 maintenance schedules and repair history</li>
    <li>Easy-to-use tables and clear layouts</li>
    <li>Perfect for all car owners, from enthusiasts to everyday drivers</li>
  </ul>

  <p class="back-message">We hope it helps you keep your vehicle in excellent condition. Please take a moment to leave a positive review on Zorvex and share your experience if you find it helpful. Thank you!</p>
</main>
</body>
</html>
```